https://www.kreidetafel.de - a website for school website in germany for presentation/paper download

we own the webpage https://www.kreidetafel.de and we need a new webdesign (a new website logo is also possible). we want only new images and css, we don´t want to made any change to the HTML code.
we need only new images/color for a new modern look.

we want to have more trust to our user. they have to download presentation/paper
we need template for this sites:
https://www.kreidetafel.de/
https://www.kreidetafel.de/referate/englisch
https://www.kreidetafel.de/forum.php
https://www.kreidetafel.de/forum/insektenhotel/147503
https://www.kreidetafel.de/referat/latein/sokrates/14781
https://www.kreidetafel.de/schule_seminararbeit_fachliste.php?fach=127
and other sites on the website. (take a look around the website)

we don´t like white color for sublines or text. (h1/h2/strong) . in image are white Text OK.

important: we want to chance ONLY the CSS and PICS, we don´t want to remove or chance any HTML code.

after you have made a mockup of the new design and we give you a go, you have to made a package with the IMAGES and the CSS rules (text how we have to chance the current css)

Target Market(s)

Germany, Austria, Switzerland -DACH

Industry/Entity Type

School

Coding

Coded - Design and coding required

Number of Pages Required

5+ page

Font styles to use
Serif
Sans Serif

Colors

Designer to choose colors to be used in the design.

Requirements
Must have
• We want only to remove images and no HTML Code
Should not have
• NO white colors for Text on the site. In images are OK

```html
<!DOCTYPE html>
<html lang="en">
<head>
<meta charset="utf-8">
<title>Kreidetafel.de – Home</title>
<link rel="stylesheet" href="https://fonts.googleapis.com/css2?family=Open+Sans:wght@400;600;700&family=Roboto:wght@400;500&display=swap">
<style>
:root{
  --olive:#8a9a17;
  --olive-dark:#6f7d10;
  --orange:#e39b12;
  --ink:#2b2b2b;
  --muted:#555;
  --line:#dcdcdc;
  --header-bg:#ededeb;
  --panel-bg:#f3f3f3;
  --footer:#363636;
  --stage:#e9e9e9;
}
*{box-sizing:border-box;margin:0;padding:0}
html,body{width:1200px;height:823px;overflow:hidden}
body{font-family:"Open Sans",Arial,sans-serif;color:var(--ink);background:linear-gradient(90deg,#dcdcdc,#f2f2f2 50%,#dcdcdc);position:relative}
.page{position:absolute;left:127px;top:0;width:946px;height:764px;background:#fff}
.deco-books{position:absolute;left:0;top:553px;width:127px;height:123px;background:linear-gradient(180deg,#8b8a78,#5e8a8c 55%,#646a70)}
.deco-student{position:absolute;left:1073px;top:220px;width:127px;height:483px;background:linear-gradient(180deg,#b8634a,#f0c9a8 30%,#e9822f 65%,#8e9aa1)}
.site-header{position:absolute;left:117px;top:9px;width:964px;height:94px;background:var(--header-bg)}
.site-header::before,.site-header::after{content:"";position:absolute;top:94px;border-top:10px solid #8a8a8a}
.site-header::before{left:0;border-right:10px solid transparent}
.site-header::after{right:0;border-left:10px solid transparent}
.brand{position:absolute;left:41px;top:18px}
.brand-name{font-size:34px;font-weight:600;color:var(--olive-dark);line-height:1}
.brand-tag{font-size:9px;color:var(--olive);margin-top:5px}
.search{position:absolute;left:381px;top:24px;width:253px;height:43px;border:1px solid #9a9a9a;background:#fff;display:flex;align-items:center;justify-content:space-between;padding:0 16px}
.search span{font-size:8.5px;font-style:italic;color:#555;text-transform:uppercase}
.btn-login{position:absolute;left:843px;top:16px;width:83px;height:28px;border-radius:14px;background:var(--olive);color:#fff;font-weight:700;font-size:12px;display:flex;align-items:center;justify-content:center}
.main-nav{position:absolute;left:657px;top:55px;display:flex;align-items:center;font-size:10px;font-weight:700}
.main-nav a{color:var(--ink);text-decoration:none}
.main-nav .active{background:var(--orange);color:#fff;border-radius:10px;width:58px;height:19px;display:flex;align-items:center;justify-content:center;margin-right:25px}
.main-nav .sp{margin-right:43px}
.side-box{position:absolute;left:149px;width:187px;border:1px solid var(--line);background:#fff}
.right{left:868px}
.box-title{background:var(--olive);color:#fff;font-weight:700;font-size:12.5px;height:30px;display:flex;align-items:center;padding-left:12px}
.center-title{justify-content:center;padding:0}
.box-list{list-style:none;font-size:11px;color:var(--ink)}
.box-list li{height:22.6px;display:flex;align-items:center;padding-left:17px;border-bottom:1px solid var(--line)}
.box-list li:last-child{border-bottom:0}
.box-list li::before{content:"";border-left:4px solid #333;border-top:3px solid transparent;border-bottom:3px solid transparent;margin-right:9px}
.box-list.pad{padding:6px 0}
.stat-key{width:75px}
.member{display:flex;padding:11px 13px;position:relative;height:76px}
.avatar{width:38px;height:38px;background:linear-gradient(#b98d6a,#6e5442)}
.badge{position:absolute;left:11px;top:53px;background:var(--orange);color:#fff;font-size:7.5px;font-weight:700;padding:2px 4px;border-radius:7px}
.member-info{margin-left:24px;font-size:9px;line-height:15px}
.member-info b{font-weight:400;font-size:11px}
.welcome{position:absolute;left:377px;top:127px;width:420px}
.welcome-kicker{font-size:11px}
.welcome-title{font-size:28px;font-weight:400;color:var(--olive);line-height:1.2;margin-top:2px}
.welcome-title strong{font-weight:700}
.welcome p{font-size:12.5px;line-height:19.6px;color:#333;margin-top:9px}
.count{margin-top:16px;font-size:12px}
.count strong{font-size:17px;color:var(--olive);margin-right:6px}
.count-note{font-size:12px;margin-top:18px;margin-left:2px}
.subjects{position:absolute;left:377px;top:355px;width:459px;height:357px;background:var(--panel-bg);border:1px solid var(--line);padding:23px 28px}
.subjects h2{font-size:14px;font-weight:400;line-height:21px}
.subject-grid{display:grid;grid-template-columns:142px 144px 1fr;row-gap:0;margin-top:25px;font-family:Roboto,Arial,sans-serif;font-size:11px}
.subject-grid span{height:30px}
.subject-grid em{font-style:normal;color:var(--olive)}
.messenger-body{padding:16px 23px 0;font-size:11px;color:#444;line-height:15px}
.pill{display:flex;align-items:center;justify-content:center;width:150px;height:35px;border-radius:18px;font-weight:700;font-size:11.5px;margin:0 auto}
.pill.fill{background:var(--orange);color:#fff;margin-top:11px}
.pill.outline{border:1px solid #bbb;color:var(--olive);margin-top:9px}
.no-msg{text-align:center;font-size:11px;margin:10px 0 8px}
.photo{height:211px;background:linear-gradient(135deg,#d9b98f,#f1dcc5 50%,#c88d5c)}
.join{text-align:center;font-size:14px;margin-top:11px}
.join-btn{display:flex;align-items:center;justify-content:center;margin:9px auto 0;width:167px;height:33px;border-radius:17px;background:var(--orange);color:#fff;font-weight:700;font-size:14px}
.online{position:absolute;left:895px;top:686px;font-size:11px;display:flex;align-items:center}
.online::before{content:"";width:8px;height:8px;border-radius:50%;background:#2da646;margin-right:9px}
.site-footer{position:absolute;left:0;top:764px;width:1200px;height:59px;background:var(--footer);color:#eee;font-family:Roboto,Arial,sans-serif;font-size:10px;display:flex;justify-content:center;padding-top:24px}
</style>
</head>
<body>
<div class="deco-books" role="img" aria-label="Illustration of a stack of books"></div>
<div class="deco-student" role="img" aria-label="Illustration of a student with glasses holding books"></div>
<div class="page"></div>

<header class="site-header">
  <div class="brand">
    <div class="brand-name">Kreidetafel.de</div>
    <div class="brand-tag">Referate, Hausaufgaben und nette Leute kennen lernen</div>
  </div>
  <div class="search"><span>Search keyword</span>
    <svg width="13" height="13" viewBox="0 0 13 13"><circle cx="5.5" cy="5.5" r="4.2" fill="none" stroke="#6f7d10" stroke-width="1.8"/><line x1="8.6" y1="8.6" x2="12" y2="12" stroke="#6f7d10" stroke-width="2"/></svg>
  </div>
  <div class="btn-login">LOGIN</div>
  <nav class="main-nav"><a class="active">HOME</a><a class="sp">COMMUNITY</a><a>PRESENTATIONS</a></nav>
</header>

<aside class="side-box" style="top:128px">
  <div class="box-title">COMMUNITY</div>
  <ul class="box-list"><li>Register</li><li>Member Login</li><li>Chat</li><li>Flirtsuche</li><li>Forum</li></ul>
</aside>
<aside class="side-box" style="top:291px">
  <div class="box-title">SCHOOL &amp; UNIVERSITY</div>
  <ul class="box-list pad"><li>Speeches / Housework</li></ul>
</aside>
<aside class="side-box" style="top:365px">
  <div class="box-title">INFORMATION</div>
  <ul class="box-list pad"><li>FAQs</li></ul>
</aside>
<aside class="side-box" style="top:440px">
  <div class="box-title">STATISTICS</div>
  <ul class="box-list">
    <li><span class="stat-key">members</span>: 401325</li>
    <li><span class="stat-key">Men</span>: 197695</li>
    <li><span class="stat-key">women</span>: 196799</li>
    <li><span class="stat-key">presentations</span>: 12458</li>
    <li><span class="stat-key">posts</span>: 3080848</li>
  </ul>
</aside>
<aside class="side-box" style="top:608px">
  <div class="box-title center-title">NEW MEMBER</div>
  <div class="member">
    <div class="avatar" role="img" aria-label="Member profile photo"></div>
    <span class="badge">PROFILE</span>
    <div class="member-info"><b>Lumi_07</b><br>Female<br>Age: 17 years</div>
  </div>
</aside>

<main>
  <section class="welcome">
    <div class="welcome-kicker">WELCOME TO</div>
    <h1 class="welcome-title">KREIDETAFEL<strong>.DE</strong></h1>
    <p>On Kreidetafel.de you will find many papers , specialist work and homework. If you are not able to find a presentation on a topic, you can ask your question in the forum where you are usually helped quickly.</p>
    <div class="count"><strong>401325</strong>members</div>
    <div class="count-note">are already registered with us!</div>
  </section>
  <section class="subjects">
    <h2>Presentations - Homework -<br>Homework for the following subjects:</h2>
    <div class="subject-grid">
      <span>English <em>(2937)</em></span><span>Chemistry <em>(450)</em></span><span>Art <em>(265)</em></span>
      <span>Latin <em>(275)</em></span><span>Astronomy <em>(82)</em></span><span>Religion <em>(521)</em></span>
      <span>French <em>(196)</em></span><span>Geography <em>(785)</em></span><span>Computer science <em>(191)</em></span>
      <span>Italian <em>(32)</em></span><span>History <em>(1870)</em></span><span>Stenography <em>(6)</em></span>
      <span>Greek <em>(196)</em></span><span>Social Science <em>(555)</em></span><span>Housekeeping <em>(109)</em></span>
      <span>Spanish <em>(74)</em></span><span>Business <em>(435)</em></span><span>Sport <em>(136)</em></span>
      <span>Mathematics <em>(99)</em></span><span>Right <em>(109)</em></span><span>Choir <em>(19)</em></span>
      <span>Physics <em>(481)</em></span><span>Music <em>(448)</em></span><span>Orchestra <em>(5)</em></span>
    </div>
  </section>
</main>

<aside class="side-box right" style="top:128px">
  <div class="box-title">LIVE MESSENGER</div>
  <div class="messenger-body">This feature is only available for members.</div>
  <div class="pill fill">CONTACT US</div>
  <div class="pill outline">LOGIN</div>
  <div class="no-msg">No new message</div>
</aside>
<aside class="side-box right" style="top:343px;height:325px">
  <div class="box-title center-title">DEIN KREIDETAFEL.DE</div>
  <div class="photo" role="img" aria-label="Photo of three smiling students giving a thumbs up"></div>
  <div class="join">Schen dabei?</div>
  <div class="join-btn">Kostenios registrieren</div>
</aside>
<div class="online">193 members online</div>

<footer class="site-footer">Home | Department of School - Housework | imprint | data protection | Conditions</footer>
</body>
</html>
```